rose gold typography style landscape business card | upmarket tanning lounge

After years of receiving spray tans, we are two young professionals starting our own spray tanning business. Our point of difference is offering a complete tanning experience within a fun, edgy yet professional atmosphere.
Our ideal card would draw upon design elements from the typography example we have attached. We are hoping to have "velmira" in all lowercase in the typography style, with "TANNING LOUNGE" in much smaller uppercase font underneath but closely positioned below "velmira".
We have attached an example of a business card created by a designer on here - we like how the word on the front almost goes beyond the edges of the card itself.
But you have the design know how, so please let your creative juices flow!
We are thinking either rose gold text (matte rather than a chrome look) with a white background or rose gold freehand style typography with a charcoal background using landscape orientation. We have opted for a thicker style edgy typography to accommodate the metallic look font we are looking for.
We cannot wait to see what you create! Thanks in advance.
Harriet & Jocelyn
Project Deadline Extended
Reason: Firstly, we wish to thank each and every one of you who have provided a submission for our project. You guys are amazingly talented and we've loved watching all the designs come through.
We have decided to take our top four favourite designs to a poll with our friends and family and will therefore need to extend the deadline by a couple of days.
We do apologise for any inconvenience this may have caused and thank you for your patience and understanding!
Harriet & Jocelyn

```html
<!DOCTYPE html>
<html lang="en">
<head>
<meta charset="utf-8">
<title>velmira — business cards</title>
<link href="https://fonts.googleapis.com/css2?family=Share+Tech&display=swap" rel="stylesheet">
<style>
  :root {
    --backdrop: #eef0ef;
    --card-light: #ffffff;
    --card-dark: #262425;
    --rose-gold: #d4846a;
    --ink-dark: #1c1b1b;
    --ink-light: #f4f1ef;
    --shadow: rgba(0, 0, 0, 0.22);
  }
  * { margin: 0; padding: 0; box-sizing: border-box; }
  html, body {
    width: 1200px;
    height: 1200px;
    overflow: hidden;
    background: var(--backdrop);
  }
  .sheet {
    position: relative;
    width: 1200px;
    height: 1200px;
  }
  .card {
    position: absolute;
    left: 248px;
    width: 733px;
    height: 419px;
    overflow: hidden;
    box-shadow: 12px 12px 6px var(--shadow);
    font-family: "Share Tech", sans-serif;
  }
  .card--light { top: 155px; background: var(--card-light); }
  .card--dark  { top: 617px; background: var(--card-dark); }

  .card__name {
    position: absolute;
    left: -14px;
    top: -38px;
    font-size: 262px;
    line-height: 1;
    font-weight: 400;
    letter-spacing: -4px;
    color: var(--rose-gold);
    white-space: nowrap;
  }
  .card__tagline {
    position: absolute;
    left: 486px;
    top: 272px;
    font-size: 14px;
    letter-spacing: 3.5px;
    text-transform: uppercase;
    white-space: nowrap;
  }
  .card--light .card__tagline { color: var(--ink-dark); }
  .card--dark  .card__tagline { color: var(--ink-light); }
</style>
</head>
<body>
  <main class="sheet">
    <section class="card card--light" aria-label="Business card, white">
      <p class="card__name">velmira</p>
      <p class="card__tagline">Tanning Lounge</p>
    </section>
    <section class="card card--dark" aria-label="Business card, charcoal">
      <p class="card__name">velmira</p>
      <p class="card__tagline">Tanning Lounge</p>
    </section>
  </main>
</body>
</html>
```